Equipment Finance Specialist I work with companies who need the funds to buy their equipment

I would like a business card that stands out on the shelves. I want to be able to hand it to someone and say WOW. This card should have my logo.
You can put color into it I am very open on design and color

What my company does is we deal with dealerships that sell equipment such as Dump Trucks garbage trucks tractors trailers. Customers get referred to us and depending on their time in business we will ask for the following items

Companies that have been in business for more than two years we have a credit application program up to 250K . With this program we need the following items Credit application filled out(which is what I would like to be able for the customer to click on my website to get.) as well as three current month bank statements.

Deals over 250k we will need the following items

2 years business tax returns
2 years personal tax returns
Profit & Loss statement
Personal Financial Statement

what we do
100% FINANCING
SEASONAL PAYMENTS
LOAN BALLOON PAYMENTS
TRAC LEASING
LOW-INTEREST REFINANCING RATES
DEBT CONSOLIDATION

We specialize in creative financing solutions and offer a variety of reliable, flexible and expandable lending choices.

Target Market(s)

Trucking Companies

Industry/Entity Type

Trucking Company

Contact Information for Business Card

* $250,000 Application only Program
* Loans from $30,000 to 5,000,000
* Competitive Interest Rates

Font styles to use
Serif
Sans Serif

Colors

Designer to choose colors to be used in the design.

Requirements
Must have
• On the back of the card.
• * $250,000 Application only Program
• * Loans from $30,000 to 5,000,000
• My name, email, website. address
• * Competitive Interest Rates
• * 100% Financing
Nice to have
• I want my logo to pop on the card
• My logo is the great one I would like to use
Should not have
• I am up for your creativity as well

```html
<!DOCTYPE html>
<html lang="en">
<head>
<meta charset="utf-8">
<title>Keystone Lending – Business Card</title>
<link href="https://fonts.googleapis.com/css2?family=Saira:wght@400;500;700;800&family=Share+Tech+Mono&display=swap" rel="stylesheet">
<style>
  :root {
    --stage: #3a3a3a;
    --card: #2b2b2b;
    --card-edge: #232323;
    --ink: #ffffff;
    --ink-soft: #e6e6e6;
    --silver: #d6d6d6;
    --accent: #e0202e;
    --ghost: rgba(255,255,255,0.05);
  }
  * { box-sizing: border-box; margin: 0; padding: 0; }
  html, body {
    width: 1200px; height: 900px; overflow: hidden;
    background: var(--stage);
    font-family: "Saira", sans-serif;
    color: var(--ink);
  }
  .stage {
    width: 1200px; height: 900px;
    display: flex; flex-direction: column;
    align-items: center; justify-content: center; gap: 30px;
  }
  .card {
    position: relative; width: 700px; height: 400px;
    background: var(--card);
    border: 1px solid var(--card-edge);
    overflow: hidden;
  }

  /* Front */
  .offer-list {
    position: absolute; top: 22px; left: 28px;
    list-style: none;
    font-family: "Share Tech Mono", monospace;
    font-size: 15px; line-height: 1.15; color: var(--ink-soft);
  }
  .offer-list li::before { content: "*"; }
  .brand {
    position: absolute; left: 0; right: 0; top: 110px;
    display: flex; flex-direction: column; align-items: center;
  }
  .brand-dot {
    width: 150px; height: 150px; border-radius: 50%;
    background: var(--silver);
  }
  .brand-name {
    margin-top: 18px;
    font-weight: 800; font-size: 58px; letter-spacing: 3px;
    text-transform: uppercase; color: var(--silver); line-height: 1;
  }

  /* Back */
  .holder { position: absolute; top: 36px; left: 48px; }
  .holder-name { font-weight: 700; font-size: 30px; line-height: 1.1; }
  .holder-name .surname { color: var(--accent); }
  .holder-role { font-weight: 700; font-size: 15px; margin-top: 2px; }
  .rule {
    position: absolute; top: 132px; left: 48px; right: 40px;
    height: 2px; background: var(--accent);
  }
  .contact-list {
    position: absolute; top: 160px; left: 48px; list-style: none;
    font-size: 21px; font-weight: 500;
  }
  .contact-list li { display: flex; align-items: center; gap: 18px; height: 46px; }
  .contact-list svg, .address svg { width: 20px; height: 20px; fill: var(--accent); flex: none; }
  .address {
    position: absolute; left: 400px; top: 270px;
    display: flex; gap: 16px; font-size: 21px; font-weight: 500; line-height: 1.75;
  }
  .address svg { margin-top: 8px; }
  .ghost-mark {
    position: absolute; right: -50px; bottom: -70px;
    width: 300px; height: 300px; border-radius: 50%;
    background: var(--ghost);
  }
</style>
</head>
<body>
<main class="stage">
  <section class="card card-front">
    <ul class="offer-list">
      <li>$250,000 Application only Program</li>
      <li>Loans from $30,000 to 5,000,000</li>
      <li>Competitive Interest Rates</li>
      <li>100% Financing</li>
    </ul>
    <div class="brand">
      <div class="brand-dot"></div>
      <div class="brand-name">Keystone Lending</div>
    </div>
  </section>

  <section class="card card-back">
    <div class="ghost-mark"></div>
    <div class="holder">
      <div class="holder-name">Marcus <span class="surname">Hale</span></div>
      <div class="holder-role">Founder | CEO</div>
    </div>
    <div class="rule"></div>
    <ul class="contact-list">
      <li><svg viewBox="0 0 24 24"><path d="M6.6 10.8a15 15 0 0 0 6.6 6.6l2.2-2.2a1 1 0 0 1 1-.25 11.4 11.4 0 0 0 3.6.57 1 1 0 0 1 1 1V20a1 1 0 0 1-1 1A17 17 0 0 1 3 4a1 1 0 0 1 1-1h3.5a1 1 0 0 1 1 1c0 1.25.2 2.45.57 3.57a1 1 0 0 1-.25 1z"/></svg>+64 (0)9555 0148</li>
      <li><svg viewBox="0 0 24 24"><path d="M3 8c0-2 4-4 9-4s9 2 9 4v2h-5V8H8v2H3z"/><path d="M5 12h14l1 8H4zm7 2a2.5 2.5 0 1 0 0 5 2.5 2.5 0 0 0 0-5z"/></svg>021 555 0173</li>
      <li><svg viewBox="0 0 24 24"><path d="M2 5h20v14H2zm2 2v.5l8 5.5 8-5.5V7z"/></svg>info@keystonelending.co</li>
      <li><svg viewBox="0 0 24 24"><path d="M12 2a10 10 0 1 0 0 20 10 10 0 0 0 0-20zm-1 2.1V8H7.3A8 8 0 0 1 11 4.1zm2 0A8 8 0 0 1 16.7 8H13zM4.6 10H11v4H4.6a8 8 0 0 1 0-4zm8.4 0h6.4a8 8 0 0 1 0 4H13zm-5.7 6H11v3.9A8 8 0 0 1 7.3 16zm5.7 0h3.7a8 8 0 0 1-3.7 3.9z"/></svg>www.keystonelending.co</li>
    </ul>
    <div class="address">
      <svg viewBox="0 0 24 24"><path d="M12 2a7 7 0 0 0-7 7c0 5 7 13 7 13s7-8 7-13a7 7 0 0 0-7-7zm0 9.5A2.5 2.5 0 1 1 12 6.5a2.5 2.5 0 0 1 0 5z"/></svg>
      <p>48 Harbour View Lane,<br>Greenlane, Auckland 1051, NZ</p>
    </div>
  </section>
</main>
</body>
</html>
```